Marketing Flyer for Plumber Referals

8.5" x11" Layout should be landscape not portrait. Create a bold, eye-catching flyer that highlights earning potential from referrals for water damage restoration. Use high-contrast colors like blue, yellow, and white, with bold fonts and dynamic layouts. Include images of restoration work, cash, and happy clients. Emphasize key benefits like $500 minimum payouts, fast payments, and unlimited income potential. Keep instructions simple: refer a client, we handle the work, you get paid. Add a clear call-to-action and display contact details prominently. Focus on professionalism and energy.

Target Market(s)

Plumbers and Contractor 8.5" x11" Layout should be landscape not portrait.

Industry/Entity Type

General Contractor

Colors
0054AA
0677BA
7BADD7
CADEEF
E8F1F8
EB3D1F
EC4F4E
F09395
F8D3D4
FCEDEE

Requirements
Must have
• 8.5" x11" Layout should be landscape not portrait.
Nice to have

```html
<!DOCTYPE html>
<html lang="en">
<head>
<meta charset="utf-8">
<title>Referral Flyer – Harborline Renovation</title>
<link rel="stylesheet" href="https://fonts.googleapis.com/css2?family=Archivo:wdth,wght@125,900&family=Poppins:wght@400;500;600;700;800&family=Questrial&display=swap">
<style>
  :root{
    --ink:#121212;
    --frame:#616161;
    --swoosh:#8c8c8c;
    --blue:#0054AA;
    --blue-bright:#0677BA;
    --navy:#123a7a;
    --red:#EB3D1F;
    --yellow:#F6C21A;
    --white:#ffffff;
  }
  *{margin:0;padding:0;box-sizing:border-box}
  html,body{width:728px;height:1200px;overflow:hidden;background:var(--frame)}
  .canvas{position:relative;width:728px;height:1200px;background:var(--frame)}
  .panel{position:absolute;left:0;width:728px;height:562px;overflow:hidden}
  .panel--earn{top:25px}
  .panel--how{top:600px}
  .panel svg.backdrop{position:absolute;inset:0}

  .brand{position:absolute;left:39px;top:84px;width:190px;text-align:center;color:var(--white);
    font-family:'Poppins',sans-serif;font-weight:500;font-size:15px;letter-spacing:1.5px;line-height:1.35}
  .brand__mark{display:block;width:12px;height:12px;border:2px solid var(--white);border-radius:50%;margin:0 auto 8px}

  .headline{position:absolute;left:266px;font-family:'Archivo',sans-serif;font-weight:900;font-stretch:125%;text-transform:uppercase;white-space:nowrap}
  .headline > span{display:block}
  .earn{top:14px;font-size:52px;line-height:46px}
  .earn .w1{color:var(--white)}
  .earn .w2{color:var(--red)}
  .earn .w3{color:var(--blue-bright)}
  .earn__side{position:absolute;left:473px;top:110px;color:var(--white);font-family:'Poppins',sans-serif;font-size:21px;line-height:20px}
  .earn__side b{font-weight:600;display:block}
  .earn__side span{font-weight:400;display:block}

  .get{top:36px;font-size:41px;line-height:37px}
  .get .white{color:var(--white)}
  .get .red{color:var(--red)}
  .get .yellow{color:var(--yellow)}

  .benefits{position:absolute;left:322px;top:206px;width:400px;color:var(--white)}
  .benefits h2{font-family:'Poppins',sans-serif;font-weight:800;font-size:22.5px;line-height:26px;text-align:center;letter-spacing:.5px;margin-left:-12px}
  .benefit{position:relative;padding-left:16px;margin-bottom:3px}
  .benefit svg{position:absolute;left:0;top:2px}
  .benefit h3{font-family:'Poppins',sans-serif;font-weight:800;font-size:16.5px;line-height:16px;color:var(--yellow)}
  .benefit p{font-family:'Questrial',sans-serif;font-size:15.5px;line-height:14.5px;max-width:375px}

  .payout{position:absolute;left:297px;top:407px;font-family:'Poppins',sans-serif;font-weight:800;font-size:43px;line-height:37px;white-space:nowrap}
  .payout .amount{color:var(--red);display:block}
  .payout .min{color:var(--blue);display:block}
  .payout .per{color:var(--blue);display:block;margin-top:2px}
  .payout .per small{font-size:25px}

  .tab{position:absolute;left:0;right:0;bottom:0;height:35px;display:flex;align-items:center;justify-content:center;
    color:var(--white);font-family:'Poppins',sans-serif;font-weight:600;font-size:21px;letter-spacing:1.5px}
  .tab--web{font-weight:500;letter-spacing:2px}

  .steps{position:absolute;left:321px;top:181px;width:400px;color:var(--white)}
  .steps h2{font-family:'Poppins',sans-serif;font-weight:700;font-size:28px;line-height:30px;text-align:right;padding-right:28px;margin-bottom:6px}
  .step{position:relative;padding-left:20px;margin-bottom:6px}
  .step svg{position:absolute;left:0;top:2px}
  .step h3{font-family:'Poppins',sans-serif;font-weight:700;font-size:18.6px;line-height:19px;color:var(--yellow);white-space:nowrap}
  .step p{font-family:'Poppins',sans-serif;font-weight:500;font-size:18.5px;line-height:19px;max-width:372px}

  .contact{position:absolute;left:353px;top:433px;color:var(--ink);font-family:'Poppins',sans-serif}
  .contact__label{font-weight:800;font-size:21px;line-height:20px;margin-left:6px}
  .contact__phone{display:flex;align-items:center;gap:8px;margin-top:6px;color:var(--navy);font-weight:800;font-size:42px;line-height:36px;letter-spacing:-1px}
</style>
</head>
<body>
<main class="canvas">
  <svg width="0" height="0" style="position:absolute" aria-hidden="true">
    <defs>
      <linearGradient id="happyClient" x1="0" y1="0" x2="0" y2="1">
        <stop offset="0" stop-color="#5a5a5e"/><stop offset=".55" stop-color="#c9c9cc"/><stop offset="1" stop-color="#8f9a84"/>
      </linearGradient>
      <linearGradient id="floodScene" x1="0" y1="0" x2="0" y2="1">
        <stop offset="0" stop-color="#e7e4df"/><stop offset=".5" stop-color="#bfb6a6"/><stop offset="1" stop-color="#6c6a66"/>
      </linearGradient>
      <linearGradient id="leakPipe" x1="0" y1="0" x2="1" y2="1">
        <stop offset="0" stop-color="#f2f2f2"/><stop offset="1" stop-color="#9a9a9a"/>
      </linearGradient>
      <linearGradient id="cashRain" x1="0" y1="0" x2="1" y2="1">
        <stop offset="0" stop-color="#1a1d18"/><stop offset=".5" stop-color="#8d9a7f"/><stop offset="1" stop-color="#1a1d18"/>
      </linearGradient>
    </defs>
  </svg>

  <section class="panel panel--earn">
    <svg class="backdrop" width="728" height="562" viewBox="0 0 728 562" aria-hidden="true">
      <rect width="728" height="562" fill="var(--ink)"/>
      <path d="M240,222 C400,178 560,160 728,158 L728,172 C560,175 420,188 265,230 Z" fill="var(--swoosh)"/>
      <path d="M262,220 C420,182 580,166 728,163 L728,482 C600,420 450,392 298,388 Z" fill="var(--blue)"/>
      <path d="M0,398 L298,398 C460,404 610,448 728,508 L728,562 L0,562 Z" fill="var(--white)"/>
      <path d="M298,386 C450,390 600,420 728,480 L728,508 C610,448 460,404 298,398 Z" fill="var(--red)"/>
      <path d="M39,562 L54,533 Q58,527 66,527 L662,527 Q670,527 674,533 L688,562 Z" fill="var(--red)"/>
      <circle cx="120" cy="333" r="182" fill="var(--white)"/>
      <circle cx="120" cy="333" r="172" fill="url(#happyClient)" role="img" aria-label="Excited young man holding a fan of cash beside a leaking pipe"/>
    </svg>

    <div class="brand"><span class="brand__mark"></span>HARBORLINE<br>RENOVATION</div>

    <h1 class="headline earn"><span class="w1">Earn</span><span class="w2">Unlimited</span><span class="w3">Cash</span></h1>
    <p class="earn__side"><b>GET PAID</b><span>TO REFER A FLOOD</span></p>

    <div class="benefits">
      <h2>WHY PARTNER WITH US?</h2>
      <div class="benefit">
        <svg width="11" height="11" viewBox="0 0 12 12"><circle cx="6" cy="6" r="5" fill="none" stroke="#fff" stroke-width="1.4"/><path d="M3.6,6.2 L5.3,7.8 L8.5,4.4" fill="none" stroke="#fff" stroke-width="1.4"/></svg>
        <h3>GUARANTEED PAYOUT:</h3><p>Minimum $500 or 10% of the invoice, paid fast.</p>
      </div>
      <div class="benefit">
        <svg width="11" height="11" viewBox="0 0 12 12"><circle cx="6" cy="6" r="5" fill="none" stroke="#fff" stroke-width="1.4"/><path d="M3.6,6.2 L5.3,7.8 L8.5,4.4" fill="none" stroke="#fff" stroke-width="1.4"/></svg>
        <h3>FREE EVALUATIONS:</h3><p>We assess damage and process insurance claims for your clients.</p>
      </div>
      <div class="benefit">
        <svg width="11" height="11" viewBox="0 0 12 12"><circle cx="6" cy="6" r="5" fill="none" stroke="#fff" stroke-width="1.4"/><path d="M3.6,6.2 L5.3,7.8 L8.5,4.4" fill="none" stroke="#fff" stroke-width="1.4"/></svg>
        <h3>INDUSTRY LEADERS:</h3><p>Certified experts with 24/7 rapid response.</p>
      </div>
      <div class="benefit">
        <svg width="11" height="11" viewBox="0 0 12 12"><circle cx="6" cy="6" r="5" fill="none" stroke="#fff" stroke-width="1.4"/><path d="M3.6,6.2 L5.3,7.8 L8.5,4.4" fill="none" stroke="#fff" stroke-width="1.4"/></svg>
        <h3>AFFORDABLE SOLUTIONS:</h3><p>Lowest out-of-pocket costs for your customers.</p>
      </div>
    </div>

    <p class="payout"><span class="amount">$500</span><span class="min">Minimum</span><span class="per"><small>or </small>10% Per <small>Referral!</small></span></p>

    <p class="tab">Send Referrals | Get Paid | Grow Your Business</p>
  </section>

  <section class="panel panel--how">
    <svg class="backdrop" width="728" height="562" viewBox="0 0 728 562" aria-hidden="true">
      <rect width="728" height="562" fill="var(--ink)"/>
      <rect x="487" y="0" width="241" height="158" fill="url(#cashRain)" role="img" aria-label="Hundred-dollar bills falling through the air"/>
      <path d="M240,222 C400,178 560,160 728,158 L728,172 C560,175 420,188 265,230 Z" fill="var(--swoosh)"/>
      <path d="M262,220 C420,182 580,166 728,163 L728,476 C600,420 470,392 340,388 Z" fill="var(--blue)"/>
      <path d="M0,398 L340,398 C470,402 610,440 728,506 L728,562 L0,562 Z" fill="var(--white)"/>
      <path d="M340,386 C470,390 600,420 728,474 L728,506 C610,440 470,402 340,398 Z" fill="var(--red)"/>
      <path d="M39,562 L54,533 Q58,527 66,527 L662,527 Q670,527 674,533 L688,562 Z" fill="var(--red)"/>
      <circle cx="120" cy="333" r="182" fill="var(--white)"/>
      <circle cx="120" cy="333" r="172" fill="url(#floodScene)" role="img" aria-label="Flooded living room with water rising up a staircase"/>
      <circle cx="264" cy="429" r="84" fill="var(--white)"/>
      <circle cx="264" cy="429" r="78" fill="url(#leakPipe)" role="img" aria-label="White drain pipe leaking water"/>
    </svg>

    <div class="brand"><span class="brand__mark"></span>HARBORLINE<br>RENOVATION</div>

    <h1 class="headline get"><span class="white">Get</span><span><span class="red">Paid to </span><span class="yellow">Refer</span></span><span class="white">A Flood</span></h1>

    <div class="steps">
      <h2>How It Works</h2>
      <div class="step">
        <svg width="15" height="15" viewBox="0 0 12 12"><circle cx="6" cy="6" r="5" fill="none" stroke="#fff" stroke-width="1.2"/><path d="M3.6,6.2 L5.3,7.8 L8.5,4.4" fill="none" stroke="#fff" stroke-width="1.2"/></svg>
        <h3>Refer Flood, Water and Mold Damage</h3><p>Call, book online, or text us directly.</p>
      </div>
      <div class="step">
        <svg width="15" height="15" viewBox="0 0 12 12"><circle cx="6" cy="6" r="5" fill="none" stroke="#fff" stroke-width="1.2"/><path d="M3.6,6.2 L5.3,7.8 L8.5,4.4" fill="none" stroke="#fff" stroke-width="1.2"/></svg>
        <h3>We Take Care of Everything</h3><p>Free evaluations, insurance claims, and professional service.</p>
      </div>
      <div class="step">
        <svg width="15" height="15" viewBox="0 0 12 12"><circle cx="6" cy="6" r="5" fill="none" stroke="#fff" stroke-width="1.2"/><path d="M3.6,6.2 L5.3,7.8 L8.5,4.4" fill="none" stroke="#fff" stroke-width="1.2"/></svg>
        <h3>Get Paid Fast</h3><p>$500 minimum or 10% of the invoice within 48 hours of final payment.</p>
      </div>
    </div>

    <div class="contact">
      <p class="contact__label">Call Text or<br>Book On-line</p>
      <p class="contact__phone">
        <svg width="26" height="26" viewBox="0 0 24 24" aria-hidden="true"><path d="M6.6,2.5 L9.4,5.6 C9.9,6.1 9.9,6.9 9.4,7.4 L7.9,8.9 C8.9,11.4 12.6,15.1 15.1,16.1 L16.6,14.6 C17.1,14.1 17.9,14.1 18.4,14.6 L21.5,17.4 C22,17.9 22,18.7 21.5,19.2 L19.6,21.1 C18.6,22.1 16.6,22.3 13.8,20.6 C9.6,18.1 5.9,14.4 3.4,10.2 C1.7,7.4 1.9,5.4 2.9,4.4 L4.8,2.5 C5.3,2 6.1,2 6.6,2.5 Z" fill="var(--navy)"/><path d="M14,3.5 A7,7 0 0 1 20.5,10 M14,6.5 A4,4 0 0 1 17.5,10" fill="none" stroke="var(--navy)" stroke-width="1.8" stroke-linecap="round"/></svg>
        555-014-2290
      </p>
    </div>

    <p class="tab tab--web">www.HarborlineRenovation.com</p>
  </section>

</main>
</body>
</html>
```